New Zealand Luggage Importer Needs Business Cards

We need professional, creative and fashionable business cards created.
We are based in New Zealand and import and distribute high-end, quality, fashionable and durable luggage.
We pride ourselves on selling the very best quality luggage, second only to 1 brand (which we won't mention here)...we use the same manufacturer. However, our prices are much more reasonable.
Industry/Entity Type
Business
Contact Information for Business Card
Mark Dunsley
027 512 4068
3/17 Harlow Street, Pinecrest Flats, Auckland, 0614
PO Box 204377, Fernside, Auckland 0731
09-528-3916
sales@brivancases.co.nz / www.brivancases.co.nz

```html
<!DOCTYPE html>
<html lang="en">
<head>
<meta charset="utf-8">
<title>Brivan Cases – Business Card</title>
<link rel="stylesheet" href="https://fonts.googleapis.com/css2?family=Montserrat:wght@500;600;800&display=swap">
<style>
  :root {
    --backdrop: #1c1c1c;
    --card-black: #221f1f;
    --card-white: #ffffff;
    --band: #231f1f;
    --ink: #1a1a1a;
    --gold: #c9a14a;
    --band-text: #f2f2f2;
  }
  * { box-sizing: border-box; margin: 0; padding: 0; }
  html, body { width: 1200px; height: 852px; overflow: hidden; }
  body {
    background: var(--backdrop);
    font-family: "Montserrat", Arial, sans-serif;
    position: relative;
  }
  .card {
    position: absolute;
    left: 280px;
    width: 640px;
    height: 366px;
    border-radius: 18px;
    overflow: hidden;
    box-shadow: 0 10px 30px rgba(0,0,0,0.5);
  }
  .card--back { top: 30px; background: var(--card-black); }
  .card--front { top: 446px; background: var(--card-white); }

  .brand-name {
    position: absolute;
    font-weight: 800;
    letter-spacing: 2px;
    white-space: nowrap;
  }
  .card--back .brand-name {
    color: #ffffff;
    font-size: 52px;
    left: 0; right: 0; top: 150px;
    text-align: center;
  }
  .card--front .brand-name {
    color: var(--ink);
    font-size: 54px;
    left: 56px; top: 112px;
  }

  .contact-band {
    position: absolute;
    left: 0; right: 0;
    top: 212px;
    height: 74px;
    background: var(--band);
    display: flex;
    align-items: center;
    padding: 0 28px 0 40px;
    gap: 26px;
  }
  .person-name {
    color: var(--gold);
    font-weight: 600;
    font-size: 28px;
    letter-spacing: 0.5px;
    white-space: nowrap;
    margin-right: 6px;
  }
  .contact-list { list-style: none; display: flex; flex-direction: column; gap: 6px; }
  .contact-list li {
    display: flex; align-items: center; gap: 7px;
    color: var(--band-text);
    font-size: 12.5px;
    font-weight: 500;
    white-space: nowrap;
  }
  .contact-list svg { width: 12px; height: 12px; flex: none; }

  .postal {
    position: absolute;
    left: 252px; top: 300px;
    font-style: normal;
    font-size: 12.5px;
    font-weight: 500;
    line-height: 1.5;
    color: var(--ink);
    white-space: nowrap;
  }
</style>
</head>
<body>

<section class="card card--back">
  <div class="brand-name">BRIVAN CASES</div>
</section>

<section class="card card--front">
  <div class="brand-name">BRIVAN CASES</div>

  <div class="contact-band">
    <h1 class="person-name">MARK DUNSLEY</h1>
    <ul class="contact-list">
      <li>
        <svg viewBox="0 0 12 12" aria-hidden="true"><rect x="3" y="0.5" width="6" height="11" rx="1" fill="none" stroke="#c9a14a" stroke-width="1.3"/><circle cx="6" cy="9.5" r="0.7" fill="#c9a14a"/></svg>
        027 512 4068
      </li>
      <li>
        <svg viewBox="0 0 12 12" aria-hidden="true"><path d="M2.5 1 L4.5 1 L5.3 3.4 L4 4.4 C4.6 5.9 6 7.3 7.6 8 L8.6 6.7 L11 7.5 L11 9.5 C11 10.4 10.3 11 9.4 11 C4.8 10.7 1.3 7.2 1 2.6 C1 1.7 1.6 1 2.5 1 Z" fill="#c9a14a"/></svg>
        09-528-3916
      </li>
    </ul>
    <ul class="contact-list">
      <li>
        <svg viewBox="0 0 12 12" aria-hidden="true"><rect x="0.5" y="2" width="11" height="8" rx="1" fill="#c9a14a"/><path d="M0.8 2.5 L6 6.5 L11.2 2.5" fill="none" stroke="#231f1f" stroke-width="1"/></svg>
        sales@brivancases.co.nz
      </li>
      <li>
        <svg viewBox="0 0 12 12" aria-hidden="true"><circle cx="6" cy="6" r="5.2" fill="none" stroke="#c9a14a" stroke-width="1.2"/><ellipse cx="6" cy="6" rx="2.2" ry="5.2" fill="none" stroke="#c9a14a" stroke-width="1"/><line x1="0.8" y1="6" x2="11.2" y2="6" stroke="#c9a14a" stroke-width="1"/></svg>
        www.brivancases.co.nz
      </li>
    </ul>
  </div>

  <address class="postal">
    3/17 Harlow Street, Pinecrest Flats, Auckland, 0614<br>
    PO Box 204377, Fernside, Auckland 0731
  </address>
</section>

</body>
</html>
```